Harborline Keys Realty business card design

Looking for an upscale and clean business card design and updated logo. I sell to a very high-end south Florida real estate market.
Target Market(s)
High-end real estate in south Florida real estate market
Industry/Entity Type
Real Estate Agent
Contact Information for Business Card
Harborline Keys Realty, Inc
738 West Pinecrest Ave, Suite 410/520, Fort Lauderdale, FL 33318
Carl Whitmore - Broker/Owner
954-555-0172 Direct
carlhomes@mailvista.example
Website: StayPinecrest.example
Font styles to use
Other font styles liked:
- Copperplate Gothic, Georgia, etc.
Requirements
Must have
- My photo, company name, my name and title, all info stated in Details above
Nice to have
- Luxury home design element, waterfront

```html
<!DOCTYPE html>
<html lang="en">
<head>
<meta charset="utf-8">
<title>Harborline Keys Realty – Business Card</title>
<link rel="stylesheet" href="https://fonts.googleapis.com/css2?family=Orbitron:wght@600&family=Open+Sans:wght@400&family=Sorts+Mill+Goudy&display=swap">
<style>
  :root {
    --backdrop: #9c9c9c;
    --card: #ffffff;
    --gold: #f5c932;
    --ink: #1a1a1a;
    --muted: #444444;
    --shadow: rgba(0, 0, 0, 0.45);
  }
  * { margin: 0; padding: 0; box-sizing: border-box; }
  html, body { width: 1200px; height: 1200px; overflow: hidden; }
  body {
    background: radial-gradient(circle at 50% 45%, #bdbdbd 0%, var(--backdrop) 70%, #7c7c7c 100%);
    position: relative;
    font-family: "Open Sans", sans-serif;
    color: var(--ink);
  }
  .card {
    position: absolute;
    background: var(--card);
    border-radius: 16px;
    box-shadow: 3px 4px 5px var(--shadow);
  }
  .card--front { left: 200px; top: 302px; width: 369px; height: 595px; }
  .card--back  { left: 600px; top: 305px; width: 363px; height: 589px; }

  .brand {
    position: absolute;
    display: flex;
    align-items: center;
    white-space: nowrap;
  }
  .brand__dot { border-radius: 50%; background: var(--gold); flex: none; }
  .card--front .brand { left: 0; right: 0; top: 280px; justify-content: center; gap: 10px; }
  .card--front .brand__dot { width: 30px; height: 30px; }
  .card--front .brand__name {
    font-family: "Sorts Mill Goudy", serif;
    font-size: 22px;
    color: var(--gold);
  }
  .card--back .brand { left: 48px; top: 118px; gap: 10px; }
  .card--back .brand__dot { width: 34px; height: 34px; }
  .card--back .brand__name {
    font-family: "Sorts Mill Goudy", serif;
    font-size: 15px;
    color: var(--ink);
  }

  .person { position: absolute; left: 72px; top: 268px; }
  .person__name {
    font-family: "Orbitron", sans-serif;
    font-weight: 600;
    font-size: 17px;
    letter-spacing: 3px;
    color: var(--gold);
    line-height: 1;
    white-space: nowrap;
  }
  .person__title { font-size: 14.5px; color: var(--muted); margin-top: 6px; }

  .contact-icons {
    position: absolute;
    left: 87px; top: 363px;
    display: flex;
    align-items: center;
    gap: 5px;
  }
  .contact-icons__rule { width: 32px; height: 1px; background: var(--ink); }
  .contact-icons__item { width: 23px; height: 23px; display: block; }

  .contact-list { position: absolute; left: 0; right: 0; top: 396px; text-align: center; }
  .contact-list__phone { font-size: 17px; line-height: 21px; }
  .contact-list__email { font-size: 14.5px; margin-top: 7px; line-height: 20px; }
  .contact-list__web { font-size: 14.5px; line-height: 22px; }

  .divider {
    position: absolute;
    left: 89px; top: 495px;
    width: 193px; height: 1px;
    background: var(--ink);
  }
  .address {
    position: absolute;
    left: 0; right: 0; top: 508px;
    text-align: center;
    font-size: 12.5px;
    line-height: 19px;
    font-style: normal;
  }
</style>
</head>
<body>
  <section class="card card--front" aria-label="Card front">
    <div class="brand">
      <span class="brand__dot"></span>
      <span class="brand__name">Harborline Keys Realty</span>
    </div>
  </section>

  <section class="card card--back" aria-label="Card back">
    <div class="brand">
      <span class="brand__dot"></span>
      <span class="brand__name">Harborline Keys Realty, Inc</span>
    </div>

    <div class="person">
      <p class="person__name">CARL WHITMORE</p>
      <p class="person__title">Broker/Owner</p>
    </div>

    <div class="contact-icons">
      <span class="contact-icons__rule"></span>
      <svg class="contact-icons__item" viewBox="0 0 24 24" aria-label="Phone">
        <rect width="24" height="24" rx="4" fill="var(--gold)"/>
        <path d="M7 5c1 0 2 2 2.5 3 .3.7-.8 1.5-1 2 .8 2 2.5 3.7 4.5 4.5.5-.2 1.3-1.3 2-1 1 .5 3 1.5 3 2.5 0 1.5-1.5 3-3 3C10 19 5 14 5 8c0-1.5 .5-3 2-3z" fill="#fff"/>
      </svg>
      <svg class="contact-icons__item" viewBox="0 0 24 24" aria-label="Fax">
        <rect width="24" height="24" rx="4" fill="var(--gold)"/>
        <rect x="7" y="4" width="10" height="5" fill="none" stroke="#fff" stroke-width="1.5"/>
        <rect x="4" y="9" width="16" height="7" rx="1" fill="#fff"/>
        <rect x="7" y="14" width="10" height="6" fill="var(--gold)" stroke="#fff" stroke-width="1.5"/>
      </svg>
      <svg class="contact-icons__item" viewBox="0 0 24 24" aria-label="Email">
        <rect width="24" height="24" rx="4" fill="var(--gold)"/>
        <rect x="4" y="6" width="16" height="12" fill="none" stroke="#fff" stroke-width="1.5"/>
        <path d="M4 6l8 7 8-7M4 18l6-6M20 18l-6-6" fill="none" stroke="#fff" stroke-width="1.3"/>
      </svg>
      <svg class="contact-icons__item" viewBox="0 0 24 24" aria-label="Website">
        <rect width="24" height="24" rx="4" fill="var(--gold)"/>
        <circle cx="12" cy="12" r="7.5" fill="none" stroke="#fff" stroke-width="1.4"/>
        <ellipse cx="12" cy="12" rx="3.2" ry="7.5" fill="none" stroke="#fff" stroke-width="1.2"/>
        <path d="M4.5 12h15M6 8h12M6 16h12" stroke="#fff" stroke-width="1.1"/>
      </svg>
      <span class="contact-icons__rule"></span>
    </div>

    <div class="contact-list">
      <p class="contact-list__phone">954-555-0172</p>
      <p class="contact-list__phone">954-555-0172</p>
      <p class="contact-list__email">carlhomes@mailvista.example</p>
      <p class="contact-list__web">StayPinecrest.example</p>
    </div>

    <div class="divider"></div>

    <address class="address">
      738 West Pinecrest Ave, Suite 410/520<br>
      Fort Lauderdale, FL 33318
    </address>
  </section>
</body>
</html>
```